Need a business card for a Construction and Remodeling company.
Our company logo is the fleur de lis design as thats the family crust that we use on our logos.
Heres the info it needs:

Brackmore Construction & Remodeling, LLC
Renovations * Restorations

Elwin R. Brackmore
845 North Quarry Road
Westbury Glen Vermont 05761
(203) 555.0182
CT LIC/REG: 418257

home owners, customers

```html
<!DOCTYPE html>
<html lang="en">
<head>
<meta charset="utf-8">
<title>Brackmore Construction &amp; Remodeling – Business Card</title>
<link rel="stylesheet" href="https://fonts.googleapis.com/css2?family=Montserrat:wght@500;600&family=Ubuntu:wght@700&display=swap">
<style>
  :root {
    --backdrop: #e9e5df;
    --card: #1c1c1e;
    --accent: #29a8e0;
    --ink: #ffffff;
  }
  * { margin: 0; padding: 0; box-sizing: border-box; }
  html, body {
    width: 1200px;
    height: 843px;
    overflow: hidden;
    background: var(--backdrop);
  }
  .card {
    position: absolute;
    left: 40px;
    top: 101px;
    width: 1120px;
    height: 640px;
    background: var(--card);
    color: var(--ink);
    font-family: "Montserrat", sans-serif;
  }
  .brand {
    position: absolute;
    left: 52px;
    top: 290px;
    width: 440px;
    text-align: center;
    color: var(--accent);
    font-weight: 600;
  }
  .brand-mark {
    display: block;
    width: 24px;
    height: 24px;
    margin: 0 auto 22px;
    background: var(--accent);
  }
  .brand-name {
    font-size: 26px;
    line-height: 32px;
    letter-spacing: 0.4px;
    white-space: nowrap;
  }
  .brand-sub {
    font-size: 34px;
    line-height: 36px;
    white-space: nowrap;
  }
  .divider {
    position: absolute;
    left: 559px;
    top: 218px;
    width: 2px;
    height: 206px;
    background: var(--accent);
  }
  .contact-name {
    position: absolute;
    left: 644px;
    top: 206px;
    font-family: "Ubuntu", sans-serif;
    font-weight: 700;
    font-size: 35px;
    line-height: 40px;
    letter-spacing: -0.3px;
    color: var(--accent);
    white-space: nowrap;
  }
  .contact-address {
    position: absolute;
    left: 644px;
    top: 279px;
    font-style: normal;
    font-weight: 600;
    font-size: 26px;
    line-height: 32px;
    letter-spacing: 2px;
    white-space: nowrap;
  }
  .contact-phone {
    position: absolute;
    left: 644px;
    top: 395px;
    display: flex;
    align-items: center;
    gap: 14px;
    font-weight: 600;
    font-size: 26px;
    line-height: 32px;
    letter-spacing: 2px;
    white-space: nowrap;
  }
  .contact-phone svg { width: 27px; height: 27px; fill: var(--accent); }
  .license {
    position: absolute;
    left: 0;
    right: 0;
    top: 507px;
    text-align: center;
    font-weight: 500;
    font-size: 26px;
    line-height: 32px;
    letter-spacing: 3px;
  }
  .services {
    position: absolute;
    left: 0;
    right: 0;
    top: 553px;
    text-align: center;
    font-weight: 600;
    font-size: 25px;
    line-height: 32px;
    letter-spacing: 2.8px;
    white-space: nowrap;
  }
  .services .sep { color: var(--accent); font-weight: 500; padding: 0 2px; }
</style>
</head>
<body>
  <main class="card">
    <div class="brand">
      <span class="brand-mark"></span>
      <div class="brand-name">BRACKMORE CONSTRUCTION</div>
      <div class="brand-sub">&amp; Remodeling, LLC</div>
    </div>

    <div class="divider"></div>

    <h1 class="contact-name">Elwin R. Brackmore</h1>
    <address class="contact-address">
      845 North Quarry Road<br>
      Westbury Glen<br>
      Vermont 05761
    </address>
    <p class="contact-phone">
      <svg viewBox="0 0 24 24" aria-hidden="true"><path d="M6.6 10.8c1.4 2.8 3.8 5.1 6.6 6.6l2.2-2.2c.3-.3.7-.4 1-.2 1.1.4 2.3.6 3.6.6.6 0 1 .4 1 1V20c0 .6-.4 1-1 1C10.6 21 3 13.4 3 4c0-.6.4-1 1-1h3.5c.6 0 1 .4 1 1 0 1.3.2 2.5.6 3.6.1.3 0 .7-.2 1z"/></svg>
      (203) 555-0182
    </p>

    <p class="license">LIC/REG: 418257</p>
    <p class="services">Renovations <span class="sep">|</span>Additions<span class="sep">|</span> Restorations</p>
  </main>
</body>
</html>
```